MBE Ad to drive teacher course enrollment

I need a relatively simple ad that is a color 4.75" w X 6" h PDF. I am attaching a poorly designed sample that I put together with the appropriate text, our branding guidelines, and a sample of a more polished ad (not ours) that appeared in the same publication for reference. I am also attaching our logo file and a couple of possible photos. We can include one photo or no photo, but not two photos. If you would like some other photo options please let me know.

Requirements
Must have
• Our logo, the dates and enrollment address as a focus, must keep the headline sentences together "Advance your students' thinking through writing" "Learn to embed the Valdrick Method in any subject"
Nice to have
• Clean design, white space
Should not have
• Images blocking words, too many color text

```html
<!DOCTYPE html>
<html lang="en">
<head>
<meta charset="UTF-8">
<title>MBE – Deeper Reasoning With Writing</title>
<link href="https://fonts.googleapis.com/css2?family=Raleway:ital,wght@0,300;0,400;0,500;0,700;0,800;1,400;1,500;1,700&display=swap" rel="stylesheet">
<style>
  :root {
    --orange: #ec5a2b;
    --navy: #1d2a52;
    --blue: #3ea4dc;
    --link-blue: #6aaee0;
    --grey: #555;
    --white: #ffffff;
  }
  * { margin: 0; padding: 0; box-sizing: border-box; }
  html, body { width: 951px; height: 1200px; overflow: hidden; background: var(--white); }
  .ad {
    position: relative;
    width: 951px; height: 1200px;
    font-family: "Raleway", sans-serif;
    background: var(--white);
    overflow: hidden;
  }
  .hero-photo {
    position: absolute; left: 0; top: 0;
    width: 951px; height: 854px;
    background:
      radial-gradient(ellipse at 68% 30%, #d9b8a0 0%, rgba(217,184,160,0) 40%),
      radial-gradient(ellipse at 88% 60%, #e0a21f 0%, rgba(224,162,31,0) 45%),
      radial-gradient(ellipse at 15% 35%, #b8aea8 0%, rgba(184,174,168,0) 50%),
      linear-gradient(180deg, #8a7a70 0%, #c9a988 45%, #e4d8cc 85%, #f1ece6 100%);
  }
  .headline-band {
    position: absolute; left: 0; top: 44px;
    width: 876px; height: 140px;
    background: rgba(255,255,255,0.86);
  }
  .headline {
    position: absolute; left: 43px; top: 62px;
    color: var(--orange);
    line-height: 1;
  }
  .headline .lead {
    display: block;
    font-weight: 800; font-size: 41px; letter-spacing: 1.4px;
  }
  .headline .follow {
    display: block; margin-top: 18px;
    font-weight: 400; font-size: 43px; letter-spacing: 1.6px;
  }
  .subhead {
    position: absolute; left: 53px; top: 200px;
    color: var(--white);
    font-style: italic; font-weight: 400; font-size: 29px;
    line-height: 35px; letter-spacing: 0.6px;
    text-shadow: 0 1px 3px rgba(0,0,0,0.25);
  }
  .subhead strong { font-weight: 700; font-style: italic; }
  .offer-badge {
    position: absolute; left: 32px; top: 557px;
    width: 270px; height: 270px;
    border-radius: 50%;
    background: var(--orange);
    border: 8px solid var(--blue);
    color: var(--white);
    text-align: center;
    display: flex; flex-direction: column; justify-content: center;
    font-size: 21px; line-height: 27px; font-weight: 500;
  }
  .offer-badge .big { font-weight: 700; font-size: 24px; line-height: 30px; }
  .rule {
    position: absolute; left: 0; top: 854px;
    width: 951px; height: 10px;
    background: var(--orange);
  }
  .registration {
    position: absolute; left: 43px; top: 906px;
    color: var(--navy);
  }
  .registration .label {
    font-weight: 700; font-size: 23px; letter-spacing: 1.2px; line-height: 28px;
  }
  .registration .course { font-size: 23px; line-height: 31px; font-weight: 500; }
  .registration .dates-label { margin-top: 10px; font-weight: 700; font-size: 23px; line-height: 31px; }
  .registration .dates { font-size: 23px; line-height: 31px; font-weight: 500; }
  .enroll {
    position: absolute; left: 43px; top: 1091px;
    color: var(--navy); font-size: 25px; font-weight: 500;
  }
  .enroll .domain-accent { color: var(--link-blue); }
  .credits {
    position: absolute; left: 43px; top: 1133px;
    color: var(--grey); font-size: 17px; font-weight: 400;
  }
  .credits em { font-weight: 700; }
  .brand {
    position: absolute; left: 626px; top: 1046px;
    width: 290px;
    display: flex; align-items: center; gap: 12px;
  }
  .brand-name {
    color: var(--blue); font-weight: 500; font-size: 26px; line-height: 29px;
  }
  .brand-dot {
    flex: none; width: 46px; height: 46px; border-radius: 50%;
    border: 4px solid var(--blue);
  }
  .brand-tagline {
    position: absolute; left: 634px; top: 1136px;
    color: var(--navy); font-size: 15px; font-weight: 500;
  }
</style>
</head>
<body>
  <div class="ad">
    <div class="hero-photo" role="img" aria-label="Photo of a student in glasses and a yellow cardigan writing in a notebook at a library desk"></div>

    <div class="headline-band"></div>
    <h1 class="headline">
      <span class="lead">ADVANCE YOUR STUDENTS’ THINKING</span>
      <span class="follow">THROUGH WRITING</span>
    </h1>

    <p class="subhead">Learn to Embed<br>the <strong>Valdrick Method</strong><br>into any Subject</p>

    <div class="offer-badge">
      <span class="big">REGISTER<br>EARLY</span>
      <span>Before courses<br>reach capacity</span>
      <span class="big">10% DISCOUNT</span>
      <span>with the code:</span>
      <span class="big">EDU</span>
    </div>

    <div class="rule"></div>

    <section class="registration">
      <h2 class="label">COURSE REGISTRATION</h2>
      <p class="course">Deeper Reasoning With Writing<br>(Grades 3-12)</p>
      <p class="dates-label">Next Courses Begin:</p>
      <p class="dates">October 12 and December 12th</p>
    </section>

    <p class="enroll">Enroll at <span class="domain-accent">mindfulbridgeed</span>.org/courses</p>
    <p class="credits"><em>Mindful Bridge Education</em> is an approved provider of CTLE credits.</p>

    <div class="brand">
      <span class="brand-name">Mindful Bridge<br>Education</span>
      <span class="brand-dot"></span>
    </div>
    <p class="brand-tagline">Bridging Ideas Into Clear Words</p>
  </div>
</body>
</html>
```